Kestrel Builders Business Card Design Project

Clean sharp business card
Ability to write on back of card
Details for the card -
Address: PO Box 5867, Corrabin, Qld, 4186
ABN: 47 305 961 220
BSA LIC 2650874
Ph: 07 3562 4470
Fax: 07 3562 4475
Email: kestrelbuilders@mailbrook.com.au

```html
<!DOCTYPE html>
<html lang="en">
<head>
<meta charset="utf-8">
<title>Kestrel Builders Business Card</title>
<link rel="stylesheet" href="https://fonts.googleapis.com/css2?family=Libre+Baskerville:wght@400;700&display=swap">
<style>
  :root {
    --card-black: #000000;
    --card-white: #ffffff;
    --accent-orange: #ec7d22;
    --brand-silver: #d4d4d4;
    --text-dark: #111111;
  }
  html, body {
    margin: 0;
    padding: 0;
    width: 1200px;
    height: 726px;
    overflow: hidden;
    background: var(--card-black);
  }
  .business-card {
    position: relative;
    width: 1200px;
    height: 726px;
    background: var(--card-black);
    overflow: hidden;
    font-family: "Libre Baskerville", Georgia, serif;
  }
  .card-panel {
    position: absolute;
    inset: 0;
    width: 1200px;
    height: 726px;
  }
  .brand-name {
    position: absolute;
    left: 72px;
    top: 112px;
    display: flex;
    align-items: center;
    gap: 16px;
    margin: 0;
    font-weight: 700;
    font-size: 42px;
    color: var(--brand-silver);
    letter-spacing: 0.5px;
  }
  .brand-dot {
    width: 22px;
    height: 22px;
    border-radius: 50%;
    background: var(--accent-orange);
  }
  .contact-block {
    position: absolute;
    right: 68px;
    top: 474px;
    text-align: right;
    color: var(--text-dark);
  }
  .postal-address {
    font-weight: 700;
    font-size: 37px;
    line-height: 1;
    margin: 0 0 34px;
    white-space: nowrap;
  }
  .contact-line {
    font-weight: 400;
    font-size: 24px;
    line-height: 1;
    margin: 0 0 20px;
    white-space: nowrap;
  }
  .divider {
    color: var(--accent-orange);
    margin: 0 10px;
  }
</style>
</head>
<body>
  <main class="business-card">
    <svg class="card-panel" viewBox="0 0 1200 726" aria-hidden="true">
      <path class="accent-band" fill="var(--accent-orange)"
        d="M1200,330 C1000,300 820,292 680,296 C430,304 160,370 70,450 C10,510 60,640 220,726 L270,726 C130,650 90,560 140,490 C230,390 480,340 700,334 C900,330 1080,345 1200,365 Z"/>
      <path class="white-panel" fill="var(--card-white)"
        d="M1200,365 C1080,345 900,330 700,334 C480,340 230,390 140,490 C90,560 130,650 270,726 L1200,726 Z"/>
    </svg>

    <h1 class="brand-name"><span class="brand-dot"></span>Kestrel Builders</h1>

    <section class="contact-block">
      <p class="postal-address">PO Box 5867, Corrabin, Qld, 4186</p>
      <p class="contact-line">ABN: 47 305 961 220<span class="divider">|</span>BAS LIC 2650874</p>
      <p class="contact-line">T. 35624470<span class="divider">|</span>F. 35624475<span class="divider">|</span>E. kestrelbuilders@mailbrook.com.au</p>
    </section>
  </main>
</body>
</html>
```